Pantry Circle is an online food market place that connects foodies who make or grow great food with

We would like a 1/2 A4 page size flyer in landscape to promote our new business. We would like to encourage new home foodies to sign up for a membership on our website www.pantrycirclenz.co.nz and we would like customers who are looking for great food in their local community to search our website for their closest home foodie and support a neighbour who is growing or producing creative food locally

Target Market(s)

Creative food lovers

Industry/Entity Type

Landscape

Colors
acd037
f78f20
33b8a4

Requirements
Must have
• Food images and look groovy
• Must be easy to read and stand out on a notice board
• Website address www.pantrycirclenz.co.nz
Nice to have
• We wish to use this flyer in multiple locations and wish to put in different contact details prior to printing

```html
<!DOCTYPE html>
<html lang="en">
<head>
<meta charset="utf-8">
<title>Pantry Circle – Flyer</title>
<link href="https://fonts.googleapis.com/css2?family=Roboto+Condensed:wght@700&family=Arimo:wght@700&family=PT+Sans:wght@400&display=swap" rel="stylesheet">
<style>
  :root {
    --backdrop: #1d1d1f;
    --paper: #f3f5f3;
    --brown-dark: #3f2312;
    --earth: #8a6a53;
    --green: #2f8f3d;
    --green-light: #7cc242;
    --green-deep: #23903a;
    --white: #ffffff;
  }
  * { margin: 0; padding: 0; box-sizing: border-box; }
  html, body {
    width: 1200px; height: 999px; overflow: hidden;
    background: var(--backdrop);
  }
  .flyer {
    position: absolute; left: 55px; top: 114px;
    width: 1090px; height: 770px;
    background: var(--paper);
    overflow: hidden;
  }
  .flyer-shapes { position: absolute; inset: 0; }
  .headline-intro, .headline-main, .headline-sub {
    position: absolute; white-space: nowrap;
  }
  .headline-intro {
    left: 79px; top: 24px;
    font: 700 41px/1 "Roboto Condensed", sans-serif;
    color: var(--brown-dark);
  }
  .headline-main {
    left: 77px; top: 80px;
    font: 700 80px/1 "Roboto Condensed", sans-serif;
    color: var(--green);
    letter-spacing: -0.5px;
  }
  .headline-sub {
    left: 84px; top: 172px;
    font: 700 40px/52px "Arimo", sans-serif;
    color: var(--brown-dark);
  }
  .headline-sub span { display: block; }
  .headline-sub span + span { padding-left: 45px; }
  .brand {
    position: absolute; left: 700px; top: 66px;
    display: flex; align-items: center; gap: 12px;
  }
  .brand-dot {
    width: 26px; height: 26px; border-radius: 50%;
    background: var(--green);
  }
  .brand-name {
    font: 700 40px/1 "Roboto Condensed", sans-serif;
    color: var(--brown-dark);
  }
  .copy {
    position: absolute;
    font: 400 19px/26px "PT Sans", sans-serif;
  }
  .copy-sellers {
    left: 196px; top: 284px; width: 290px;
    text-align: center; color: #1a1a1a;
  }
  .copy-buyers {
    left: 25px; top: 462px; width: 190px;
    color: var(--white);
  }
  .copy-contact {
    left: 250px; top: 708px; width: 292px;
    text-align: center; color: var(--white);
  }
</style>
</head>
<body>
  <section class="flyer">
    <svg class="flyer-shapes" width="1090" height="770" viewBox="0 0 1090 770">
      <defs>
        <linearGradient id="kitchenTone" x1="0" y1="0" x2="1" y2="1">
          <stop offset="0" stop-color="#e9e4df"/>
          <stop offset="0.45" stop-color="#c9b8a8"/>
          <stop offset="0.75" stop-color="#8aa0c4"/>
          <stop offset="1" stop-color="#9cc070"/>
        </linearGradient>
        <linearGradient id="swoopGreen" x1="0" y1="1" x2="1" y2="0">
          <stop offset="0" stop-color="var(--green-deep)"/>
          <stop offset="0.5" stop-color="var(--green-light)"/>
          <stop offset="1" stop-color="var(--green-deep)"/>
        </linearGradient>
      </defs>
      <path class="earth-field" fill="var(--earth)"
            d="M0,240 C120,370 250,480 425,590 L795,770 L0,770 Z"/>
      <path class="kitchen-photo" role="img"
            aria-label="Photo of a smiling couple preparing a fresh salad in a bright kitchen with vegetables on the counter"
            fill="url(#kitchenTone)"
            d="M425,590 L795,770 L1090,770 L1090,160 C800,240 600,360 425,590 Z"/>
      <path class="edge-line" fill="none" stroke="var(--green-deep)" stroke-width="4"
            d="M425,590 L795,770"/>
      <path class="swoop-left" fill="url(#swoopGreen)"
            d="M0,55 C90,240 230,420 440,600 C260,480 120,370 0,240 Z"/>
      <path class="swoop-main" fill="url(#swoopGreen)"
            d="M105,770 C350,470 700,250 1090,154 C780,250 560,390 420,570 C340,670 280,720 230,770 Z"/>
    </svg>

    <h1 class="headline-intro">Be part of our exciting new online</h1>
    <p class="headline-main">food marketplace</p>
    <p class="headline-sub"><span>connecting foodies in your</span><span>local community</span></p>

    <div class="brand">
      <span class="brand-dot"></span>
      <span class="brand-name">Pantry Circle</span>
    </div>

    <p class="copy copy-sellers">As a foodie you can sell your beautiful home produced or home grown produce on our marketplace website</p>
    <p class="copy copy-buyers">As a food lover you can purchase lovingly grown or prepared food and support your local foodie community while keeping your food miles low</p>
    <p class="copy copy-contact">For more information go to:<br>www.pantrycirclenz.co.nz</p>
  </section>
</body>
</html>
```